Property Management Company

We are looking for a sharp/modern business card design for a property management company.
We have included what should be on the business card down below in business card details.
Target Market(s)
Commercial properties, Home Owners
Industry/Entity Type
Business
Contact Information for Business Card
Name: Colin Basford | Owner
Business Name : Tern Yardworks
Slogan : A Smarter Choice
Phone : 518.555.0183
Website: www.ternyardworks.example
E-Mail : colin@ternyardworks.example
Our Services are Commercial & Residential
-Asphalt Maintenance
-Snow Management
-Landscaping
-Blacktop
Free Estimates
Free parking lot cleanup & restripe with snow removal contract

```html
<!DOCTYPE html>
<html lang="en">
<head>
<meta charset="utf-8">
<title>Tern Yardworks – Business Card</title>
<link href="https://fonts.googleapis.com/css2?family=Quicksand:wght@400;500;700&display=swap" rel="stylesheet">
<style>
  :root {
    --backdrop: #e7e3dc;
    --card: #f4f1e6;
    --navy: #2e4a78;
    --red: #c8202f;
    --green: #1f9a4e;
    --ink: #8a8780;
    --ink-strong: #6f6c66;
    --band-text: #f4f1e6;
  }
  * { margin: 0; padding: 0; box-sizing: border-box; }
  html, body { width: 1200px; height: 1000px; overflow: hidden; }
  body {
    background: var(--backdrop);
    font-family: "Quicksand", sans-serif;
    position: relative;
  }
  .card {
    position: absolute;
    left: 230px;
    width: 740px;
    height: 422px;
    background: var(--card);
    border-radius: 20px;
    overflow: hidden;
    box-shadow: 0 10px 30px rgba(0,0,0,0.15);
  }
  .card--front { top: 44px; }
  .card--back { top: 534px; }

  .lockup {
    position: absolute;
    display: flex;
    flex-direction: column;
    align-items: center;
    color: var(--green);
  }
  .brand {
    display: flex;
    align-items: center;
    gap: 14px;
    font-weight: 700;
    white-space: nowrap;
  }
  .brand__mark {
    width: 30px; height: 30px;
    background: var(--navy);
  }
  .slogan {
    font-weight: 700;
    white-space: nowrap;
  }
  .card--front .lockup {
    left: 0; right: 0; top: 130px;
  }
  .card--front .brand { font-size: 54px; }
  .card--front .slogan { font-size: 26px; margin-top: 4px; padding-left: 44px; }

  .card--back .lockup {
    right: 46px; top: 136px;
  }
  .card--back .brand { font-size: 40px; }
  .card--back .brand__mark { width: 24px; height: 24px; }
  .card--back .slogan { font-size: 20px; margin-top: 2px; padding-left: 38px; }

  .band {
    position: absolute;
    left: 0; right: 0; bottom: 0;
    height: 48px;
    display: flex;
    align-items: center;
    padding: 0 36px;
    color: var(--band-text);
    font-size: 17px;
    font-weight: 500;
    letter-spacing: 0.3px;
    white-space: nowrap;
  }
  .band--red { background: var(--red); }
  .band--navy { background: var(--navy); justify-content: flex-end; }

  .contact {
    position: absolute;
    left: 48px; top: 56px;
    width: 330px;
    color: var(--ink);
  }
  .contact__name {
    font-size: 24px;
    font-weight: 700;
    color: var(--ink-strong);
    padding-left: 30px;
  }
  .contact__role {
    font-size: 17px;
    padding-left: 30px;
    margin-bottom: 18px;
  }
  .contact__row {
    display: flex;
    align-items: flex-start;
    gap: 12px;
    font-size: 16px;
    line-height: 1.45;
    margin-bottom: 10px;
    white-space: nowrap;
  }
  .contact__icon {
    width: 18px; height: 18px;
    flex: 0 0 18px;
    margin-top: 2px;
    fill: none;
    stroke: var(--ink);
    stroke-width: 1.6;
  }
</style>
</head>
<body>

<section class="card card--front">
  <div class="lockup">
    <div class="brand"><span class="brand__mark"></span>Tern Yardworks</div>
    <div class="slogan">A Smarter Choice</div>
  </div>
  <div class="band band--red">Commercial &amp; Residential -Asphalt Maintenance</div>
</section>

<section class="card card--back">
  <div class="contact">
    <div class="contact__name">Colin Basford</div>
    <div class="contact__role">Owner</div>
    <div class="contact__row">
      <svg class="contact__icon" viewBox="0 0 24 24"><path d="M5 3h4l2 5-2.5 1.5a11 11 0 0 0 6 6L16 13l5 2v4a2 2 0 0 1-2 2A17 17 0 0 1 3 5a2 2 0 0 1 2-2z"/></svg>
      <span>518.555.0183</span>
    </div>
    <div class="contact__row">
      <svg class="contact__icon" viewBox="0 0 24 24"><rect x="3" y="5" width="18" height="14" rx="1"/><path d="M3 6l9 7 9-7"/></svg>
      <span>colin@ternyardworks.example<br>www.ternyardworks.example</span>
    </div>
    <div class="contact__row">
      <svg class="contact__icon" viewBox="0 0 24 24"><path d="M12 22s7-7 7-12a7 7 0 0 0-14 0c0 5 7 12 7 12z"/><circle cx="12" cy="10" r="2.5"/></svg>
      <span>Free Estimates</span>
    </div>
  </div>
  <div class="lockup">
    <div class="brand"><span class="brand__mark"></span>Tern Yardworks</div>
    <div class="slogan">A Smarter Choice</div>
  </div>
  <div class="band band--navy">Snow Management -Landscaping -Blacktop</div>
</section>

</body>
</html>
```